Webdesign für Hausmeisterservice, Garten- und Landschaftsbau
Zielgruppe
Hausmeisterservice und Garten und Landschaftsbau
Aufgabenstellung
habe schon eine Webseite erstellt die muss Designt werden. Wohnpfleger.info

```html
<!DOCTYPE html>
<html lang="de">
<head>
<meta charset="utf-8">
<title>Hausmeisterservice &amp; Housekeeping</title>
<link href="https://fonts.googleapis.com/css2?family=Barlow:wght@400;500;600&family=Fira+Sans:wght@700;800&display=swap" rel="stylesheet">
<style>
:root{
  --green:#0aa240;
  --green-dark:#0a8a3c;
  --green-light:#0cb446;
  --orange:#f7a919;
  --text:#6b6b6b;
  --heading:#0aa83d;
  --line:#dcdcdc;
  --white:#ffffff;
}
*{margin:0;padding:0;box-sizing:border-box}
html,body{width:1200px;height:4375px;overflow:hidden;background:var(--white)}
body{position:relative;font-family:"Barlow",sans-serif;color:var(--text)}
.abs{position:absolute}
h1,h2,h3{font-family:"Fira Sans",sans-serif;font-weight:800}
.top-rule{left:0;top:73px;width:1200px;height:1px;background:#bdbdbd}
.corner-mark{left:1194px;top:0;width:6px;height:26px;background:#111}
.hero{left:0;width:1200px;background:linear-gradient(90deg,var(--green-dark),var(--green-light))}
.hero-photo{width:365px;box-shadow:0 20px 30px rgba(0,0,0,.18)}
.crumb{font-size:14px;color:var(--white);display:flex;align-items:center;gap:14px}
.crumb i{display:inline-block;width:16px;height:2px;background:var(--orange)}
.hero-title{color:var(--white);font-size:62px;line-height:1;letter-spacing:.5px}
.hero-text{color:var(--white);font-size:14px;line-height:30px;font-weight:500}
.eyebrow{font-size:11px;letter-spacing:1.5px;color:var(--orange)}
.section-title{color:var(--heading);font-size:46px;line-height:46px}
.copy{font-size:14.5px;line-height:30px}
.feature-title{font-family:"Fira Sans",sans-serif;font-weight:700;font-size:17px;color:var(--heading)}
.tick-list{list-style:none;font-size:14px;line-height:31px}
.tick-list li{display:flex;align-items:center;gap:10px}
.tick{width:13px;height:13px;flex:none}
.card{background:var(--white);border-radius:4px;box-shadow:0 10px 28px rgba(0,0,0,.08);padding:32px 32px}
.card h3{font-size:20px;line-height:30px;color:var(--heading);font-weight:700;margin-bottom:18px}
.card p{font-size:14px;line-height:29px}
.more{display:inline-block;margin-top:18px;font-size:13px;color:var(--text);padding-bottom:10px;border-bottom:2px solid var(--green)}
.btn{background:var(--orange);color:#333;font-size:13px;font-weight:600;display:flex;align-items:center;justify-content:center;gap:6px;border-radius:20px 20px 0 20px}
.info-box{padding:36px 32px;border-radius:4px}
.info-box h3{font-size:20px;font-weight:700;margin-bottom:20px}
.info-box p{font-size:14px;line-height:29px}
.contact-item{font-size:14px;display:flex;flex-direction:column;gap:4px}
.contact-item span{display:flex;align-items:center;gap:8px}
.bottom-rule{left:0;top:4259px;width:1200px;height:1px;background:#bdbdbd}
</style>
</head>
<body>
<svg width="0" height="0" style="position:absolute">
  <defs>
    <symbol id="tick" viewBox="0 0 14 14"><circle cx="7" cy="7" r="7" fill="#f7a919"/><path d="M3.8 7.2l2.2 2.2 4.2-4.4" fill="none" stroke="#fff" stroke-width="1.8"/></symbol>
    <symbol id="arrow" viewBox="0 0 14 10"><path d="M0 5h12M8 1l4 4-4 4" fill="none" stroke="#6b6b6b" stroke-width="1.2"/></symbol>
    <symbol id="pin" viewBox="0 0 12 16"><path d="M6 0a6 6 0 0 1 6 6c0 4.5-6 10-6 10S0 10.5 0 6a6 6 0 0 1 6-6z" fill="#f7a919"/><circle cx="6" cy="6" r="2.2" fill="#fff"/></symbol>
    <symbol id="phone" viewBox="0 0 16 16"><path d="M3.5 1l3 3-1.8 2a9 9 0 0 0 5.3 5.3l2-1.8 3 3-2 2.5C7 14.5 1.5 9 1 3.5z" fill="#f7a919"/></symbol>
  </defs>
</svg>

<div class="abs top-rule"></div>
<div class="abs corner-mark"></div>

<!-- Hero: Hausmeisterservice -->
<section class="abs hero" style="top:83px;height:357px"></section>
<div class="abs crumb" style="left:117px;top:170px">Home <i></i> Service</div>
<h1 class="abs hero-title" style="left:117px;top:200px">Hausmeisterservice</h1>
<p class="abs hero-text" style="left:117px;top:284px;width:530px">Als Hausmeisterservice fühlen wir uns für das gesamte übertragene Objekt verantwortlich.</p>
<div class="abs hero-photo" style="left:765px;top:104px;height:364px;background:linear-gradient(160deg,#6f8f4a,#3f6a2a 60%,#8a9a6a)" role="img" aria-label="Foto: Gartenarbeit mit Schubkarre im Garten"></div>

<!-- Intro -->
<div class="abs" style="left:93px;top:616px;width:402px;height:390px;background:linear-gradient(135deg,#8c8a78,#4d6a35 55%,#7a7f62);clip-path:polygon(50% 0,100% 48%,70% 100%,0 60%,15% 38%)" role="img" aria-label="Luftbild eines gepflasterten Gartens mit Beeten"></div>
<div class="abs eyebrow" style="left:535px;top:567px">CONTACT US</div>
<h2 class="abs section-title" style="left:535px;top:598px;width:580px">Partner für alle Haus- und Wohnungsangelegenheiten!</h2>
<p class="abs copy" style="left:535px;top:725px;width:550px">Unser Hausmeisterservice ist darauf ausgerichtet, Ihnen das Leben einfacher zu machen und Ihnen die Gewissheit zu geben, dass Ihr Zuhause oder Ihre Immobilie stets in besten Händen ist. Wir kümmern uns um die Bedürfnisse von Privathaushalten, Wohnanlagen, Gewerbeobjekten und vielem mehr. Egal, ob es um regelmäßige Wartung, Reparaturen, Reinigung oder umfassende Betreuung geht – bei uns sind Sie richtig!</p>
<div class="abs feature-title" style="left:544px;top:948px">Wir sind für Sie das</div>
<ul class="abs tick-list" style="left:544px;top:986px">
  <li><svg class="tick"><use href="#tick"/></svg>alle Leistungen aus einer Hand.</li>
  <li><svg class="tick"><use href="#tick"/></svg>Individuell</li>
</ul>
<div class="abs feature-title" style="left:825px;top:948px">24 Stunden Service</div>
<ul class="abs tick-list" style="left:825px;top:986px">
  <li><svg class="tick"><use href="#tick"/></svg>24 Stunden für sie im Einsatz</li>
  <li><svg class="tick"><use href="#tick"/></svg>keine versteckten Kosten</li>
</ul>
<div class="abs" style="left:535px;top:1055px;width:560px;height:1px;background:var(--line)"></div>

<div class="abs card" style="left:95px;top:1103px;width:328px;height:336px">
  <h3>Kanal-Abfluss und Rohrreinigung</h3>
  <p>In uns finden Sie einen zuverlässigen Partner im Bereich der Abfluss-, Kanal- und Rohrreinigung. – unser qualifiziertes Fachpersonal ist für Sie in Ihrer Stadt unterwegs</p>
  <a class="more">Kontakt <svg width="12" height="9"><use href="#arrow"/></svg></a>
</div>
<div class="abs card" style="left:443px;top:1103px;width:328px;height:336px">
  <h3>Winterdienst</h3>
  <p>Schnee und Eis können zur Gefahr werden. Unser Team räumt und streut zuverlässig, um Ihre Sicherheit zu gewährleisten.</p>
  <a class="more">Kontakt <svg width="12" height="9"><use href="#arrow"/></svg></a>
</div>
<div class="abs card" style="left:791px;top:1103px;width:328px;height:336px">
  <h3>Gartenpflege</h3>
  <p>Wir sorgen für einen gepflegten Außenbereich, damit Sie sich rundum wohlfühlen können.</p>
  <a class="more">Kontakt <svg width="12" height="9"><use href="#arrow"/></svg></a>
</div>

<!-- Hero: Housekeeping -->
<section class="abs hero" style="top:1512px;height:417px"></section>
<div class="abs crumb" style="left:117px;top:1598px">Home <i style="background:#fff"></i> Housekeeping</div>
<h1 class="abs hero-title" style="left:117px;top:1630px">Housekeeping</h1>
<p class="abs hero-text" style="left:117px;top:1713px;width:615px">Unser Housekeeping-Service ist darauf ausgerichtet, Ihre Wohn- oder Geschäftsräume in einen makellosen und ansprechenden Zustand zu versetzen. Wir verstehen, dass Sauberkeit ein essentieller Bestandteil eines angenehmen und gesunden Umfelds ist, und deshalb setzen wir alles daran, Ihren Ansprüchen gerecht zu werden.</p>
<div class="abs hero-photo" style="left:765px;top:1563px;height:366px;background:linear-gradient(150deg,#e6e6e6,#b9b9b9 50%,#3a3a3a)" role="img" aria-label="Foto: Reinigung eines Backofens in der Küche"></div>

<!-- Sauberkeit -->
<h2 class="abs section-title" style="left:102px;top:2070px;width:500px">Partner für Sauberkeit, Komfort und Wohlbefinden!</h2>
<p class="abs copy" style="left:624px;top:2089px;width:480px">Wir bitten individuelle Housekeeping-Lösungen, die auf Ihre spezifischen Bedürfnisse zugeschnitten sind. Egal, ob es um Ihr Zuhause, Ihr Büro, ein Hotel oder eine Veranstaltungsfläche geht – wir passen unsere Dienstleistungen an Ihre Anforderungen an.</p>
<div class="abs feature-title" style="left:633px;top:2251px">Partnerschaft</div>
<ul class="abs tick-list" style="left:633px;top:2289px">
  <li><svg class="tick"><use href="#tick"/></svg>alle Leistungen aus einer Hand.</li>
  <li><svg class="tick"><use href="#tick"/></svg>Individuell</li>
</ul>
<div class="abs feature-title" style="left:877px;top:2251px">24 Stunden Service</div>
<ul class="abs tick-list" style="left:877px;top:2289px">
  <li><svg class="tick"><use href="#tick"/></svg>24 Stunden für sie im Einsatz</li>
  <li><svg class="tick"><use href="#tick"/></svg>keine versteckten Kosten</li>
</ul>
<a class="abs btn" style="left:624px;top:2360px;width:123px;height:41px"><svg width="13" height="13"><use href="#phone"/></svg>Anrufen</a>

<div class="abs card" style="left:110px;top:2613px;width:318px;height:272px">
  <h3>Wohn-, Schlafzimmer</h3>
  <p>Wir kümmern uns um die umfassende Reinigung Ihrer Wohnräume, damit Sie sich in Ihrem Zuhause rundum wohlfühlen können.</p>
  <a class="more">Kontakt <svg width="12" height="9"><use href="#arrow"/></svg></a>
</div>
<div class="abs card" style="left:448px;top:2613px;width:319px;height:272px">
  <h3>Badezimmer</h3>
  <p>Wir reinigen gründlich Ihr Badezimmer Kalkablagerungen werden effektiv entfernt, um hygienische Bedingungen zu gewährleisten.</p>
  <a class="more">Kontakt <svg width="12" height="9"><use href="#arrow"/></svg></a>
</div>
<div class="abs card" style="left:786px;top:2613px;width:319px;height:272px">
  <h3>Küche</h3>
  <p>Wir reinigen Ihre Küchenschränke, Schubladen und Arbeitsflächen sorgfältig, um Staub, Fett und Schmutz zu entfernen.</p>
  <a class="more">Kontakt <svg width="12" height="9"><use href="#arrow"/></svg></a>
</div>

<div class="abs card info-box" style="left:110px;top:3095px;width:487px;height:325px">
  <h3 style="color:var(--heading)">Partnerschaft</h3>
  <p>Bei uns erhalten sie durch vereinbaren einer fixen Summe alle Leistungen zuverlässig und gewissenhaft aus einer Hand. Wir sind Ihr Hausmeister vor Ort und der Ansprechpartner für Ihre Mieter oder Handwerker. Wir betreuen jedes Grundstück so individuell, als wäre es unser Eigenes. Sie haben fragen oder wünschen detaillierte Informationen zu unseren Leistungen? Dann kontaktieren sie uns direkt .</p>
</div>
<div class="abs info-box" style="left:618px;top:3095px;width:487px;height:325px;background:var(--green-light);color:#fff">
  <h3>24 Stunden Service</h3>
  <p>Wer eine Verstopfung im Abfluss bemerkt, der braucht schnelle Hilfe, daher ist unser Service 24 Stunden für sie im Einsatz. Sie werden erst über alle anfallenden Kosten informiert und dann wird mit den Arbeiten erst begonnen – keine versteckten Kosten – kostenlose Beratung.</p>
</div>

<!-- Video band -->
<div class="abs" style="left:0;top:3525px;width:1200px;height:378px;background:linear-gradient(100deg,#2f7a6a,#3d8070 45%,#3f6f52 75%,#2d6a4e)" role="img" aria-label="Foto: Verlegen von Rollrasen im Garten, grün eingefärbt"></div>
<a class="abs btn" style="left:117px;top:3703px;width:105px;height:41px">Kontakt</a>
<svg class="abs" style="left:891px;top:3686px" width="60" height="60" viewBox="0 0 60 60"><circle cx="30" cy="30" r="30" fill="#f7a919"/><path d="M25 21l13 9-13 9z" fill="#fff"/></svg>

<!-- Kontakt -->
<h2 class="abs section-title" style="left:95px;top:4024px;width:420px">Benötigen Sie Informationen?</h2>
<div class="abs contact-item" style="left:573px;top:4005px">
  <svg width="11" height="14"><use href="#pin"/></svg>
  <span><svg width="13" height="13"><use href="#phone"/></svg>+49 341 587 3310</span>
</div>
<div class="abs contact-item" style="left:851px;top:4005px">
  <svg width="11" height="14"><use href="#pin"/></svg>
  <span><svg width="13" height="13"><use href="#phone"/></svg>+49 89 214 7783</span>
</div>
<div class="abs bottom-rule"></div>
</body>
</html>
```